Covid19 Poster for workplaces

Create a poster on how to protect yourself from Corona virus at work.
We are a Brightwell Works company. We have just re-branded so we need to fit in with our brand. We like clean and fresh, slightly amusing is ok if it will draw attention but it's an important topic. A4 and A3 please.

Content:

Headline: Lower the risk of COVID 19 in the workplace.

BE WELL

Bring your own cup - don’t share cups and food.
Elbow tap instead of handshakes and kisses
Wash your hands often - with soap.
Elbow or tissues when you cough or sneeze then straight in the bin
Leave your face alone after touching shared surfaces
Leave your bugs at home if you’re feeling unwell.

Call health line if you have a cough, a high temperature and shortness of breath. 0800 472 9160

Based on recommendations from IPB and DCT

Target Market(s)

Employees - so anyone

Other font styles liked:
• Use the closest font to the brand documents

Requirements
Should not have
• Clip art

```html
<!DOCTYPE html>
<html lang="en">
<head>
<meta charset="utf-8">
<title>Lower the risk of COVID 19 in the workplace</title>
<link href="https://fonts.googleapis.com/css2?family=Montserrat:wght@500;600;700;800;900&display=swap" rel="stylesheet">
<style>
  :root {
    --teal: #1badb5;
    --teal-dark: #15959c;
    --ink: #111111;
    --panel: #e6e7e8;
    --red: #f01919;
    --white: #ffffff;
    --backdrop: #f2f2f2;
  }
  * { box-sizing: border-box; margin: 0; padding: 0; }
  html, body { width: 1200px; height: 1200px; overflow: hidden; }
  body {
    background: var(--backdrop);
    font-family: "Montserrat", Arial, sans-serif;
    color: var(--ink);
    position: relative;
  }
  .poster {
    position: absolute;
    left: 182px; top: 13px;
    width: 836px; height: 1173px;
    background: var(--white);
    overflow: hidden;
  }
  .hero-art { position: absolute; left: 0; top: 0; width: 836px; height: 580px; }
  .brand {
    position: absolute; left: 36px; top: 70px;
    display: flex; align-items: center; gap: 14px;
  }
  .brand-dot { width: 34px; height: 34px; border-radius: 50%; background: var(--teal); }
  .brand-name { font-weight: 700; font-size: 36px; line-height: 1; color: var(--ink); }
  .headline {
    position: absolute; left: 34px; top: 172px;
    font-weight: 900; font-size: 47px; line-height: 54px; letter-spacing: 0.2px;
  }
  .headline .accent { color: var(--teal); }
  .be-well {
    position: absolute; left: 310px; top: 546px;
    font-weight: 800; font-size: 39px; letter-spacing: 0.5px;
  }
  .pill {
    position: absolute; display: flex; align-items: center; gap: 10px;
    color: var(--white); font-weight: 800; font-size: 38px; border-radius: 32px;
    z-index: 2;
  }
  .pill-do { left: 310px; top: 603px; width: 192px; height: 62px; background: var(--teal); padding-left: 12px; }
  .pill-dont { left: 277px; top: 917px; width: 246px; height: 62px; background: var(--red); padding-left: 14px; }
  .pill svg { flex: none; }
  .panel { position: absolute; background: var(--panel); border-radius: 64px; }
  .panel-do { left: 27px; top: 633px; width: 784px; height: 272px; }
  .panel-dont { left: 35px; top: 946px; width: 760px; height: 200px; }
  .tip {
    position: absolute; display: flex; align-items: center; gap: 12px;
    font-weight: 600; font-size: 15.5px; line-height: 20px; letter-spacing: 0.3px;
  }
  .tip svg { flex: none; }
  .tip-dont { font-size: 18.5px; line-height: 22px; font-weight: 500; letter-spacing: 0.5px; }
  .helpline {
    position: absolute; left: 0; top: 1073px; width: 836px; height: 100px;
    background: var(--teal); color: var(--white);
    display: flex; align-items: center; justify-content: center; text-align: center;
    font-weight: 700; font-size: 21px; line-height: 27px; letter-spacing: 0.3px;
  }
</style>
</head>
<body>
<main class="poster">
  <svg class="hero-art" viewBox="0 0 836 580" aria-hidden="false">
    <defs>
      <linearGradient id="photoFade" x1="0" y1="0" x2="1" y2="0">
        <stop offset="0" stop-color="#ffffff"/>
        <stop offset="0.35" stop-color="#e9eef1"/>
        <stop offset="0.65" stop-color="#9aa6b4"/>
        <stop offset="1" stop-color="#3c4a66"/>
      </linearGradient>
      <linearGradient id="handsTone" x1="0" y1="0" x2="1" y2="1">
        <stop offset="0" stop-color="#2d3a52"/>
        <stop offset="0.5" stop-color="#c99a86"/>
        <stop offset="1" stop-color="#dfe4ea"/>
      </linearGradient>
    </defs>
    <path role="img" aria-label="Photo: commuter in a face mask coughing into his hand on a train"
          d="M250 0 H836 V440 C700 500 520 525 320 520 C200 515 80 470 0 430 V0 Z" fill="url(#photoFade)"/>
    <path d="M0 428 C90 470 210 510 330 514 C520 520 700 495 836 436 V458 C700 515 520 540 330 532 C200 528 90 490 0 446 Z" fill="var(--teal)"/>
    <path d="M0 424 C90 466 210 506 330 510 C520 516 700 490 836 432" fill="none" stroke="#111" stroke-width="2"/>
    <rect x="0" y="0" width="836" height="580" fill="url(#photoFade)" opacity="0" />
    <ellipse role="img" aria-label="Photo: two people shaking hands with virus particles" cx="190" cy="475" rx="170" ry="98" fill="url(#handsTone)" stroke="var(--teal)" stroke-width="7"/>
  </svg>

  <div class="brand">
    <span class="brand-dot"></span>
    <span class="brand-name">Brightwell Works</span>
  </div>

  <h1 class="headline">Lower the risk of<br><span class="accent">COVID 19</span> in the<br>WORKPLACE</h1>

  <div class="be-well">BE WELL</div>

  <div class="pill pill-do">
    <svg width="42" height="42" viewBox="0 0 42 42"><circle cx="21" cy="21" r="18" fill="none" stroke="#fff" stroke-width="3"/><path d="M12 21 L18.5 27.5 L30 15" fill="none" stroke="#fff" stroke-width="3.5" stroke-linecap="round" stroke-linejoin="round"/></svg>
    <span>DO’S</span>
  </div>
  <div class="panel panel-do"></div>

  <div class="tip" style="left:48px; top:703px;">
    <svg width="50" height="40" viewBox="0 0 50 40"><rect x="2" y="3" width="34" height="34" rx="5" fill="var(--teal)"/><path d="M36 12 h4 a7 7 0 0 1 0 14 h-4" fill="none" stroke="var(--teal)" stroke-width="5"/></svg>
    <span>Bring your<br>own cup</span>
  </div>
  <div class="tip" style="left:308px; top:680px;">
    <svg width="60" height="58" viewBox="0 0 60 58"><path d="M8 2 h10 l-2 34 c10 -2 24 -2 34 0 c6 2 6 14 0 16 c-14 4 -32 4 -44 0 c-6 -2 -8 -6 -8 -10 Z" fill="var(--teal)"/></svg>
    <span>Elbow tap</span>
  </div>
  <div class="tip" style="left:556px; top:680px;">
    <svg width="68" height="66" viewBox="0 0 68 66"><path d="M4 30 l18 -14 c4 -3 10 -1 12 2 l-10 10 h30 c4 0 4 6 0 6 h-6 c4 0 4 6 0 6 h-4 c4 0 4 6 0 6 h-6 c3 0 3 6 0 6 h-24 c-6 0 -10 -4 -10 -10 Z" fill="var(--teal)"/><circle cx="48" cy="10" r="5" fill="var(--teal)"/><circle cx="60" cy="16" r="3.5" fill="var(--teal)"/><circle cx="38" cy="6" r="3" fill="var(--teal)"/></svg>
    <span>Wash your hands<br>often - with soap.</span>
  </div>
  <div class="tip" style="left:30px; top:775px;">
    <svg width="74" height="84" viewBox="0 0 74 84"><circle cx="60" cy="8" r="8" fill="var(--teal)"/><path d="M50 20 h18 v40 h-5 v22 h-6 v-22 h-2 v22 h-6 v-42 l-10 8 l-4 -4 Z" fill="var(--teal)"/><path d="M2 40 h38 l-4 42 h-30 Z" fill="var(--teal)"/><rect x="0" y="34" width="42" height="5" fill="var(--teal)"/></svg>
    <span>Elbow or tissues<br>when you cough<br>or sneeze then<br>straight in the bin</span>
  </div>
  <div class="tip" style="left:310px; top:775px;">
    <svg width="58" height="60" viewBox="0 0 58 60"><path d="M30 2 c-16 0 -28 12 -28 28 c0 12 8 22 16 26 l4 -16 c-4 -2 -6 -6 -6 -10 c0 -8 6 -14 14 -14 c6 0 10 4 12 8 c4 12 4 26 14 32 h-10 c-8 -6 -8 -20 -12 -28 c4 14 2 26 -6 30 c14 -2 24 -20 22 -36 c-2 -12 -10 -20 -20 -20 Z" fill="var(--teal)"/></svg>
    <span>Leave your face<br>alone after<br>touching shared<br>surfaces</span>
  </div>
  <div class="tip" style="left:556px; top:772px;">
    <svg width="68" height="70" viewBox="0 0 68 70"><rect x="4" y="22" width="60" height="44" rx="3" fill="none" stroke="var(--teal)" stroke-width="5"/><path d="M20 30 v-14 a14 14 0 0 1 28 0 v14" fill="none" stroke="var(--teal)" stroke-width="5"/><circle cx="20" cy="32" r="3" fill="var(--teal)"/><circle cx="48" cy="32" r="3" fill="var(--teal)"/></svg>
    <span>Leave your bugs<br>at home if you’re<br>feeling unwell.</span>
  </div>

  <div class="pill pill-dont">
    <svg width="40" height="40" viewBox="0 0 40 40"><circle cx="20" cy="20" r="19" fill="#fff"/><path d="M13 13 L27 27 M27 13 L13 27" stroke="var(--red)" stroke-width="4" stroke-linecap="round"/></svg>
    <span>DON’TS</span>
  </div>
  <div class="panel panel-dont"></div>

  <div class="tip tip-dont" style="left:62px; top:1008px;">
    <svg width="62" height="38" viewBox="0 0 62 38"><path d="M2 10 h22 c8 0 16 -6 26 -8 c8 -2 12 6 4 10 c-4 2 -8 4 -10 8 c-4 8 -12 14 -24 14 h-18 Z" fill="var(--red)"/></svg>
    <span>Don’t share cups and food.</span>
  </div>
  <div class="tip tip-dont" style="left:446px; top:996px;">
    <svg width="74" height="54" viewBox="0 0 74 54"><path d="M0 8 l12 -6 l10 24 l-10 6 Z M74 8 l-12 -6 l-10 24 l10 6 Z" fill="var(--red)"/><path d="M16 28 l14 -16 c4 -4 10 -4 14 0 l14 14 l-4 4 l-10 -8 l-8 6 c-3 2 -7 0 -6 -3 l6 -8 c-4 0 -6 2 -8 4 l-8 10 c6 6 12 12 18 16 c3 2 7 -2 4 -4 c3 2 7 -2 4 -4 c3 2 7 -2 4 -4 l4 -3 l4 2 c-6 8 -16 16 -22 18 c-10 -6 -18 -14 -24 -24 Z" fill="var(--red)"/></svg>
    <span>don’t do handshakes and<br>kisses</span>
  </div>

  <footer class="helpline">
    <p>Call health line if you have a cough, a high temperature and<br>shortness of breath
      <svg width="20" height="20" viewBox="0 0 20 20" style="vertical-align:-3px"><circle cx="10" cy="10" r="8.5" fill="none" stroke="#fff" stroke-width="1.6"/><path d="M7 5.5 l2 2.5 l-1 1.2 c0.6 1.4 1.6 2.4 3 3 l1.2 -1 l2.5 2 l-1.2 1.6 c-4 -0.4 -7.4 -3.8 -7.8 -7.8 Z" fill="#fff"/></svg>
      0800 472 9160</p>
  </footer>
</main>
</body>
</html>
```